New Townhome community needs for sale sign.

need a 4 foot by 8 foot banner to put on building listing newly constructed townhomes as "coming soon" to market. Construction is scheduled to be completed Dec 2024. Sale of units will begin Spring of 2025.
6 individual townhome units each 2,000 square feet. each unit is 3 bedroom 2.5 bathroom with 2 car garage and each has a rooftop "sky lounge" with amazing views. Gated community. Units available for sale Spring of 2025. Real estate company selling units will be Qorvane & Partners. Will need Qorvane & Partners Logo on the banner. Would like to keep with the same blue color scheme as the Qorvane & Partners logo. phone number on banner to be 602-555-4179. web klmpartnersx.com.

```html
<!DOCTYPE html>
<html lang="en">
<head>
<meta charset="utf-8">
<title>Qorvane &amp; Partners – Townhomes Coming Soon</title>
<link rel="stylesheet" href="https://fonts.googleapis.com/css2?family=Montserrat:wght@400;500;600;700&display=swap">
<style>
  :root {
    --navy: #073a5a;
    --teal: #1b7897;
    --stripe: #2c6ea3;
    --paper: #e9f6fb;
    --stage: #b3b3b3;
    --white: #ffffff;
  }
  * { box-sizing: border-box; margin: 0; padding: 0; }
  html, body {
    width: 697px; height: 1200px; overflow: hidden;
    background: var(--stage);
    font-family: "Montserrat", Arial, sans-serif;
  }
  .sign-frame {
    position: absolute; left: 48px; top: 0;
    width: 588px; height: 1175px;
    transform: scale(1.0213); transform-origin: top left;
  }
  .sign {
    position: relative; width: 588px; height: 1175px;
    background: var(--paper); overflow: hidden;
  }
  .hero { position: absolute; left: 0; top: 0; width: 588px; height: 420px; }
  .brand-box {
    position: absolute; left: 170px; top: 282px; width: 250px; height: 85px;
    background: var(--white); border: 3px solid var(--stripe);
    display: flex; align-items: center; justify-content: center; gap: 9px;
  }
  .brand-mark { width: 26px; height: 26px; background: var(--stripe); flex: none; }
  .brand-name { font-size: 19px; font-weight: 600; color: var(--navy); white-space: nowrap; }
  .headline {
    position: absolute; top: 424px; width: 100%; text-align: center;
    font-size: 26px; font-weight: 600; color: var(--navy);
  }
  .coming-soon {
    position: absolute; left: 124px; top: 469px; width: 340px; height: 60px;
    background: var(--navy); color: var(--white);
    font-size: 36px; font-weight: 700; letter-spacing: 1px;
    display: flex; align-items: center; justify-content: center;
  }
  .sale-note {
    position: absolute; top: 543px; width: 100%; text-align: center;
    font-size: 16px; color: var(--navy);
  }
  .features { position: absolute; left: 62px; top: 601px; width: 500px; list-style: none; }
  .features li {
    position: relative; padding-left: 22px; margin-bottom: 29px;
    font-size: 23px; line-height: 33px; color: var(--teal); letter-spacing: 0.3px;
  }
  .features li::before { content: "•"; position: absolute; left: 0; top: 0; font-weight: 700; }
  .features strong { font-weight: 700; }
  .phone {
    position: absolute; left: 129px; top: 947px; width: 329px; height: 52px;
    background: var(--navy); color: var(--white); border-radius: 12px;
    font-size: 36px; font-weight: 700;
    display: flex; align-items: center; justify-content: center;
  }
  .availability {
    position: absolute; top: 1028px; width: 100%; text-align: center;
    font-size: 33px; color: var(--navy);
  }
  .season-band {
    position: absolute; left: 0; top: 1072px; width: 100%; height: 67px;
    background: var(--navy); color: var(--white);
    font-size: 48px; font-weight: 500;
    display: flex; align-items: center; justify-content: center;
  }
</style>
</head>
<body>
  <div class="sign-frame">
    <section class="sign">
      <svg class="hero" viewBox="0 0 588 420" xmlns="http://www.w3.org/2000/svg">
        <defs>
          <linearGradient id="townhome-tones" x1="0" y1="0" x2="0" y2="1">
            <stop offset="0" stop-color="#5f86b8"/>
            <stop offset="0.45" stop-color="#c9ccc9"/>
            <stop offset="0.75" stop-color="#7a4a30"/>
            <stop offset="1" stop-color="#5a6a70"/>
          </linearGradient>
        </defs>
        <polygon role="img" aria-label="Photo of newly built townhome buildings under a blue sky"
                 points="0,0 588,0 588,246 0,392" fill="url(#townhome-tones)"/>
        <polygon points="0,392 588,246 588,262 0,408" fill="var(--white)"/>
        <polygon points="0,400 588,254 588,266 0,420" fill="var(--stripe)"/>
      </svg>
      <div class="brand-box">
        <span class="brand-mark"></span>
        <span class="brand-name">Qorvane &amp; Partners</span>
      </div>

      <h1 class="headline">Newly Constructed Townhomes</h1>
      <div class="coming-soon">COMING SOON</div>
      <p class="sale-note">Sale of units will begin Spring of 2025.</p>

      <ul class="features">
        <li>6 individual townhome units<br>each <strong>2,000 square feet.</strong></li>
        <li>Each unit is <strong>3 bedroom<br>2.5 bathroom</strong> with <strong>2 car garage.</strong></li>
        <li>Each has a rooftop "<strong>sky lounge</strong>"<br>with amazing views.</li>
        <li><strong>Gated community.</strong></li>
      </ul>

      <div class="phone">602-555-4179</div>
      <p class="availability">Units available for</p>
      <div class="season-band">sale Spring of 2025</div>
    </section>
  </div>
</body>
</html>
```